Larkfield Institute Logo & Business card

Larkfield Institute - Professional ICT Training
business is a training center.
Logo and business card that have an ID.
bold publicity, distinct, and prestige image
"Ensure professional Success"
that will attract target customer to come and take a look. that will look prestige on certificate after graduation, that will serve as a business tool to attract Business and enterprise customer (let them send their staff for training)
Updates

upgrade to with logo vector design

Target Market(s)

young professionals, university students, youth building career in IT fields

Industry/Entity Type

Education

Contact Information for Business Card

Address
Phone
email
Facebook

Font styles to use
Sans Serif

Colors

Designer to choose colors to be used in the design.

Requirements
Must have
• Logo Identity
• uniqueness
Nice to have
• catch phrase or illustration
Should not have
• just use alphabet as logo.

```html
<!DOCTYPE html>
<html lang="en">
<head>
<meta charset="utf-8">
<title>Larkfield Institute – Business Card</title>
<link rel="stylesheet" href="https://fonts.googleapis.com/css2?family=Orbitron:wght@700;800&family=Lato:wght@400&display=swap">
<style>
  :root{
    --navy:#142c52;
    --gold:#f2b51f;
    --grey:#7a7a7a;
    --paper:#ffffff;
    --backdrop:#e7e5e1;
  }
  *{margin:0;padding:0;box-sizing:border-box}
  html,body{width:1200px;height:902px;overflow:hidden;background:var(--backdrop)}
  .stage{position:relative;width:1200px;height:902px}
  .card{
    position:absolute;left:148px;top:193px;width:903px;height:515px;
    background:var(--paper);border-radius:22px;overflow:hidden;
    box-shadow:0 6px 24px rgba(0,0,0,.12);
  }
  .brand{
    position:absolute;left:30px;top:140px;width:400px;text-align:center;
  }
  .brand-dot{
    display:block;width:80px;height:80px;margin:0 auto 22px;
    border-radius:50%;background:var(--gold);
  }
  .brand-name{
    font-family:'Orbitron',sans-serif;font-weight:800;font-size:24px;
    color:var(--navy);letter-spacing:.5px;white-space:nowrap;
  }
  .brand-tagline{
    margin-top:6px;font-family:'Orbitron',sans-serif;font-weight:700;
    font-size:12.5px;letter-spacing:3.2px;color:var(--gold);white-space:nowrap;
  }
  .divider{
    position:absolute;left:450px;top:145px;width:2px;height:222px;background:var(--gold);
  }
  .contact{position:absolute;left:490px;top:145px;font-family:'Lato',sans-serif}
  .person-name{
    font-family:'Orbitron',sans-serif;font-weight:800;font-size:23px;
    color:var(--navy);letter-spacing:1px;line-height:1;
  }
  .person-role{font-size:19px;color:var(--gold);margin-top:4px}
  .address{margin-top:14px;font-size:20px;line-height:27px;color:var(--grey)}
  .channels{list-style:none;margin-top:15px}
  .channels li{
    display:flex;align-items:center;gap:12px;font-size:19.5px;
    line-height:28px;color:var(--grey);
  }
  .channels svg{width:18px;height:18px;flex:none}
  .footer-stripe{
    position:absolute;left:0;right:0;bottom:96px;height:8px;background:var(--gold);
  }
  .footer-band{
    position:absolute;left:0;right:0;bottom:0;height:88px;background:var(--navy);
  }
</style>
</head>
<body>
<div class="stage">
  <div class="card">
    <div class="brand">
      <span class="brand-dot"></span>
      <div class="brand-name">LARKFIELD INSTITUTE</div>
      <div class="brand-tagline">Professional ICT Training</div>
    </div>

    <div class="divider"></div>

    <div class="contact">
      <div class="person-name">OWEN MERCER</div>
      <div class="person-role">Director</div>
      <div class="address">PO BOX 418, Harbour Lane<br>2nd street Westbrook</div>
      <ul class="channels">
        <li>
          <svg viewBox="0 0 18 18" aria-hidden="true"><rect x="4" y="1" width="10" height="16" rx="2" fill="none" stroke="#f2b51f" stroke-width="2"/><rect x="7" y="13" width="4" height="1.6" fill="#f2b51f"/></svg>
          (555) 018 2240
        </li>
        <li>
          <svg viewBox="0 0 18 18" aria-hidden="true"><rect x="1" y="4" width="16" height="11" fill="#f2b51f"/><path d="M1 4 L9 11 L17 4" fill="none" stroke="#fff" stroke-width="1.4"/></svg>
          info@larkfieldmail.com
        </li>
        <li>
          <svg viewBox="0 0 18 18" aria-hidden="true"><circle cx="9" cy="9" r="8" fill="#f2b51f"/><g fill="none" stroke="#fff" stroke-width="1"><ellipse cx="9" cy="9" rx="3.5" ry="8"/><line x1="1" y1="9" x2="17" y2="9"/><line x1="2.5" y1="5" x2="15.5" y2="5"/><line x1="2.5" y1="13" x2="15.5" y2="13"/></g></svg>
          www.larkfieldinstitute.com
        </li>
      </ul>
    </div>

    <div class="footer-stripe"></div>
    <div class="footer-band"></div>
  </div>
</div>
</body>
</html>
```